AMAZING WEBSITE DESIGN NEEDED FOR MAID / CLEANING SERVICE

NOTE: This is Website Design Only - No coding required

Please submit your designs ASAP as we want to pick a winner and get started!

Hey,

We are looking for a new amazing website design for a maid or cleaning service.

They have a horrible website that we want turned into a masterpiece.

As you will see on their current site:

http://tidyharborco.examplehost.net/

They have a lot of stuff, very disorganized, and need help.

Here is what we need:

Colors: Same as current site, Orange, Gray, Black

Menu: Horizontal with same Menu items

Need a spot for a video on the homepage

Want content to be structured in a great format that is easy to read.

Want to highlight commercial and residential on the website homepage.

Also want a spot for customer testimonials

We want the site clean, professional, fresh and modern.

Please help by matching the logo design.

I look forward to your designs!
Updates

Hi All! Really appreciate your efforts and designs. I will be meeting with our client on Monday and will then be able to provide feedback after our meeting. If you have other ideas, please submit them. The more I can show him the better! Thanks!

Target Market(s)

The target market is residential home owners as well as commercial businesses who need cleaning on a regular basis.

This company cleans homes and offices for individuals.

Industry/Entity Type

Residential

Font styles to use
Sans Serif

Requirements
Must have
• Must match logo colors
Must have spot for video
Must have a clean look
Must have a bold look
Nice to have
• Highly visual
Should not have
• clutter
messy design
hard to read

```html
<!DOCTYPE html>
<html lang="en">
<head>
<meta charset="utf-8">
<title>Tidy Harbor – Home</title>
<link rel="stylesheet" href="https://fonts.googleapis.com/css2?family=Dosis:wght@300;400;500;600&display=swap">
<style>
:root{
  --orange:#f47b13;
  --orange-text:#f47a12;
  --light:#f4f4f4;
  --black:#000;
  --white:#fff;
  --ink:#111;
}
*{margin:0;padding:0;box-sizing:border-box}
html,body{width:1200px;height:1000px;overflow:hidden}
body{position:relative;font-family:Verdana,"DejaVu Sans",sans-serif;background:var(--black)}
.heading{font-family:"Dosis",sans-serif;font-weight:400;text-transform:uppercase;letter-spacing:.5px;line-height:1}

/* Welcome */
.welcome{position:absolute;left:0;top:0;width:1200px;height:289px;background:var(--light);overflow:hidden}
.welcome__title{position:absolute;left:147px;top:14px;font-size:36px;color:var(--ink);z-index:1}
.welcome__text{position:absolute;left:147px;top:76px;font-size:12.9px;line-height:15.7px;color:var(--orange-text);white-space:nowrap;z-index:1}
.welcome__photo{position:absolute;left:760px;top:10px;width:370px;height:279px;z-index:0;
  background:radial-gradient(ellipse at 55% 55%,#c9d3e4 0%,#e8ebef 45%,var(--light) 75%)}

/* Orange band */
.band{position:absolute;left:0;top:289px;width:1200px;height:462px;background:var(--orange)}
.band__title{position:absolute;top:51px;font-size:35px;color:var(--white)}
.testimonials__title{left:147px}
.how__title{left:626px}
.testimonial{position:absolute;left:147px;width:440px}
.testimonial__date{position:absolute;left:0;top:0;width:61px;background:var(--black);color:var(--orange);
  font-family:"Dosis",sans-serif;text-align:center}
.testimonial__date::after{content:"";position:absolute;right:-7px;top:8px;border-left:7px solid var(--black);border-top:5px solid transparent;border-bottom:5px solid transparent}
.testimonial__day{display:block;font-size:38px;font-weight:300;margin-top:14px;line-height:1}
.testimonial__month{display:block;font-size:16px;font-weight:500;margin-top:6px;text-transform:uppercase}
.testimonial__name{position:absolute;left:79px;top:-4px;font-family:"Dosis",sans-serif;font-size:19px;font-weight:400;color:var(--ink)}
.testimonial__quote{position:absolute;left:79px;top:32px;font-size:13px;line-height:15.6px;color:var(--ink);white-space:nowrap}
.read-more{position:absolute;left:226px;top:383px;width:97px;height:37px;border-radius:3px;background:var(--black);
  color:var(--white);font-family:Arial,sans-serif;font-size:14px;line-height:37px;text-align:center}

.video{position:absolute;left:626px;top:110px;width:429px;height:261px;background:#3a3a3a}
.video__frame{position:absolute;left:0;top:0;width:429px;height:240px;
  background:linear-gradient(180deg,#444 0%,#4a4a4a 40%,#3b3b3b 100%)}
.video__bar{position:absolute;left:0;top:240px;width:429px;height:21px;background:linear-gradient(#f4f4f4,#dcdcdc)}
.video__time{position:absolute;left:48px;top:6px;font-size:8px;color:#444;font-family:Arial,sans-serif}
.video__quality{position:absolute;left:341px;top:6px;font-size:8px;color:#444;font-family:Arial,sans-serif}
.video__tip{position:absolute;left:334px;top:229px;padding:1px 4px;background:#111;border-radius:2px;color:#ddd;font-size:7px;font-family:Arial,sans-serif}

/* Footer */
.footer{position:absolute;left:0;top:751px;width:1200px;height:249px;background:var(--black);color:var(--white)}
.footer__nav{position:absolute;top:58px;list-style:none;font-family:"Dosis",sans-serif;font-weight:500;font-size:17.5px;line-height:26.7px;text-transform:uppercase;letter-spacing:.2px}
.footer__nav--one{left:149px}
.footer__nav--two{left:331px}
.footer__follow{position:absolute;left:781px;top:60px;font-size:13px}
.social{position:absolute;top:46px;width:30px;height:30px;background:var(--orange)}
.social--first{left:878px}
.social--second{left:918px}
.footer__address{position:absolute;left:781px;top:93px;font-style:normal;font-size:13.3px;line-height:15.7px}
.footer__legal{position:absolute;left:150px;top:215px;font-size:13px}
</style>
</head>
<body>

<section class="welcome">
  <div class="welcome__photo" role="img" aria-label="Photo of a smiling maid in a blue apron scrubbing the floor beside a blue bucket"></div>
  <h1 class="heading welcome__title">Welcome to Tidy Harbor</h1>
  <p class="welcome__text">Thank you for visiting us! You are one step closer to experiencing first class maid service! Our<br>
company specializes in detailed housekeeping, janitorial, and commerical cleaning services<br>
making your environment shine and sparkle like it never has before! &nbsp;Our maids are fully trained<br>
professionals who we recruit from high end luxury hotels we know, like the Grandview and Baycrest!<br>
We pride ourselves in delivering exceptional service to our valued customers by fully under-<br>
standing what your expectations &amp; needs are! We will strive for perfection and we will provide an<br>
uncompromising commitment to excellence! Our "Tidy Harbor" name gives us an edge over our<br>
competition by giving you access to more home and office cleaning services for absolutely no<br>
extra costs! Why pay more for less?? NEVER have any hidden charges, overages, or sneaky fees!<br>
With Tidy Harbor start getting more for your dollar! Your wish is our command and that is the<br>
true "Tidy Harbor" way! Call us today!</p>
</section>

<section class="band">
  <h2 class="heading band__title testimonials__title">Testimonials</h2>

  <article class="testimonial" style="top:109px;height:91px">
    <div class="testimonial__date" style="height:91px"><span class="testimonial__day">02</span><span class="testimonial__month">Jan '14</span></div>
    <h3 class="testimonial__name">Dalton Weir</h3>
    <p class="testimonial__quote">"I was very impressed with the amount they do for<br>the price! Remarkable! Thank you Tidy Harbor for<br>taking this daily headache away from my fiance.<br>She was so thrilled. See you guys again soon!</p>
  </article>

  <article class="testimonial" style="top:238px;height:122px">
    <div class="testimonial__date" style="height:122px"><span class="testimonial__day" style="margin-top:16px">21</span><span class="testimonial__month">Dec '13</span></div>
    <h3 class="testimonial__name">Marian Kessler</h3>
    <p class="testimonial__quote">"Thank you Tidy Harbor for making my house so<br>fresh and clean! How nice it was to have all of my<br>laundry washed and folded and my dishes done &amp; put<br>away along with everything else! I have requested<br>that she return next week! Oustanding you guys,<br>keep it up!</p>
  </article>

  <a class="read-more">Read More</a>

  <h2 class="heading band__title how__title">How does it works?</h2>
  <div class="video">
    <div class="video__frame" role="img" aria-label="Video still of a cleaner in a red apron scrubbing a tiled floor next to a red bucket"></div>
    <span class="video__tip">HD available in full screen</span>
    <div class="video__bar">
      <svg width="429" height="21" viewBox="0 0 429 21" aria-hidden="true">
        <rect x="0" y="0" width="429" height="3" fill="#bbb"/>
        <circle cx="4" cy="1.5" r="3.5" fill="#eee" stroke="#999"/>
        <rect x="6" y="8" width="2" height="7" fill="#333"/><rect x="10" y="8" width="2" height="7" fill="#333"/>
        <polygon points="24,10 27,10 31,7 31,16 27,13 24,13" fill="#333"/>
        <rect x="372" y="8" width="9" height="7" fill="none" stroke="#333"/>
        <path d="M395 13 a4 4 0 1 1 5 0" fill="none" stroke="#333" stroke-width="1.5"/>
        <path d="M413 8 h3 M413 8 v3 M425 8 h-3 M425 8 v3 M413 16 h3 M413 16 v-3 M425 16 h-3 M425 16 v-3" stroke="#333" stroke-width="1.3"/>
      </svg>
      <span class="video__time">0:00 / 0:53</span>
      <span class="video__quality">360p</span>
    </div>
  </div>
</section>

<footer class="footer">
  <ul class="footer__nav footer__nav--one">
    <li>Home</li><li>Services</li><li>About</li><li>Employees</li><li>Why Choose Us</li>
  </ul>
  <ul class="footer__nav footer__nav--two">
    <li>Testimonials</li><li>Request a Bid</li><li>Special Offers</li><li>Contact Us</li><li>Meet the Presidents &amp; CEO</li>
  </ul>
  <span class="footer__follow">Follow Us At</span>
  <span class="social social--first" aria-label="Social profile"></span>
  <span class="social social--second" aria-label="Social profile"></span>
  <address class="footer__address">
    Tidy Harbor<br>
    4120 Linden Ridge Road NE Suite 310<br>
    Maple Falls | Eastvale | 00421<br>
    (555) 010-2244 Office<br>
    (555) 010-3388 Fax<br>
    hello@tidyharbor.example
  </address>
  <p class="footer__legal">Tidy Harbor © 2014 | Privacy Policy</p>
</footer>

</body>
</html>
```